Jewish & Muslim Interfaith Dialogue titled "We Walk Beside" by US Non-Profit Veranth.Foundation

Residences through the USA strive for cooperative democracy within the United States of America's neighborhoods. We are for peaceful collaborations within the Western views and Muslim. We discuss the practice existence in modern society of Shariah Law in a cooperation and neighborly conservation between Muslim Imam Kamil Rotheran and Dennis Holt a Jewish retired US federal prosecutor.

Our website is currently under redesign but the logo for the foundation is current at veranth.foundation view Imam Kamil's bio at kmlrth.com

Target Market(s)

Any interested in Interfaith, Islam and Peaceful Democracy

Industry/Entity Type

Interfaith religious democratic america

Font styles to use
Sans Serif
Decorative

Requirements
Must have
• Use also some color scheme to compliment logo. Some elements from the drafted design in visuals for the worlds that are written around the book title
Nice to have
• The veranth logo and other people.
Should not have
• Any violent images

```html
<!DOCTYPE html>
<html lang="en">
<head>
<meta charset="utf-8">
<title>We Walk Beside — Kamil Rotheran &amp; Dennis Holt</title>
<link rel="stylesheet" href="https://fonts.googleapis.com/css2?family=Bebas+Neue&family=Poppins:wght@600;700&family=Ubuntu:wght@400&family=Tinos:ital@1&display=swap">
<style>
  :root{
    --ink:#005a78;
    --aqua:#4fbbcf;
    --leaf:#97b92a;
    --white:#ffffff;
    --emblem:#3f8ea8;
  }
  html,body{margin:0;padding:0;overflow:hidden;}
  body{width:800px;height:1200px;}
  .cover{
    position:relative;width:800px;height:1200px;overflow:hidden;
    font-family:"Bebas Neue",sans-serif;
  }
  .layer{position:absolute;inset:0;}
  .t{position:absolute;margin:0;line-height:1;white-space:nowrap;}
  .verb{font-family:"Poppins",sans-serif;font-weight:600;font-size:23px;color:var(--aqua);}
  .verb.low{color:var(--white);}
  .pillar{font-size:47px;color:var(--ink);letter-spacing:-0.5px;}
  .pillar.aqua{color:var(--aqua);}
  .pillar.white{color:var(--white);}
  .pillar.small{font-size:28px;}
  .note{font-family:"Ubuntu",sans-serif;font-size:17.5px;color:var(--ink);}
  .note.white{color:var(--white);}
  .charge{font-family:"Tinos",serif;font-style:italic;font-size:21.5px;color:var(--aqua);left:0;width:800px;text-align:center;}
  .charge.white{color:var(--white);font-size:17px;}
  .title{font-family:"Poppins",sans-serif;font-weight:700;left:0;width:800px;text-align:center;letter-spacing:-4px;}
  .title.ink{color:var(--ink);}
  .title.leaf{color:var(--leaf);}
  .left{left:37px;}
  .right{right:26px;text-align:right;}
  .center{left:0;width:800px;text-align:center;}
  .foundation{font-family:"Ubuntu",sans-serif;font-size:22px;color:var(--emblem);}
  .authors{font-size:33px;color:var(--ink);}
</style>
</head>
<body>
<main class="cover">
  <svg class="layer" width="800" height="1200" role="img" aria-label="Cloudy sky photograph fading from pale top through grey clouds to clear teal">
    <defs>
      <linearGradient id="skyFade" x1="0" y1="0" x2="0" y2="1">
        <stop offset="0" stop-color="#f4f1f0"/>
        <stop offset="0.24" stop-color="#f1eeed"/>
        <stop offset="0.34" stop-color="#a9b2b4"/>
        <stop offset="0.55" stop-color="#87939a"/>
        <stop offset="0.72" stop-color="#aac9d0"/>
        <stop offset="0.82" stop-color="#a3d4de"/>
        <stop offset="1" stop-color="#5cbfd1"/>
      </linearGradient>
      <radialGradient id="faintGlow" cx="0.5" cy="0.5" r="0.5">
        <stop offset="0" stop-color="#ffffff" stop-opacity="0.55"/>
        <stop offset="1" stop-color="#ffffff" stop-opacity="0"/>
      </radialGradient>
    </defs>
    <rect width="800" height="1200" fill="url(#skyFade)"/>
  </svg>

  <svg class="layer" width="800" height="1200" aria-hidden="true">
    <rect x="57" y="153" width="304" height="337" rx="40" fill="url(#faintGlow)" role="img" aria-label="Faint white Jewish faith symbol"/>
    <rect x="423" y="158" width="360" height="312" rx="40" fill="url(#faintGlow)" role="img" aria-label="Faint white Muslim faith symbol"/>
  </svg>

  <p class="t verb left" style="top:28px;">demonize</p>
  <p class="t verb center" style="top:28px;">discriminate</p>
  <p class="t verb right" style="top:28px;">discredit</p>

  <p class="t pillar left" style="top:132px;">Man Made Law</p>
  <p class="t pillar right" style="top:132px;">Divine Law</p>

  <p class="t title ink" style="top:82px;font-size:140px;">WE</p>

  <p class="t charge" style="top:236px;">Jewish Rejection Anti Semitism Radicalism Segregation Intimidation Occupation</p>

  <p class="t pillar aqua left" style="top:309px;">Politics</p>
  <p class="t note left" style="top:357px;">Conservatism</p>
  <p class="t pillar aqua right" style="top:309px;">Religion</p>
  <p class="t note right" style="top:357px;">UltraConservatism</p>

  <p class="t title leaf" style="top:330px;font-size:150px;">WALK</p>

  <p class="t pillar left" style="top:472px;">President</p>
  <p class="t note white left" style="top:520px;">UltraLiberalism</p>
  <p class="t pillar right" style="top:472px;">Caliph</p>
  <p class="t note white right" style="top:520px;">UktraConservatism</p>

  <p class="t pillar white left" style="top:577px;">Freedom</p>
  <p class="t pillar white right" style="top:577px;">Force</p>

  <p class="t foundation center" style="top:682px;">Veranth.Foundation</p>

  <p class="t pillar left" style="top:798px;">Democracy</p>
  <p class="t pillar right" style="top:798px;">Caliphate</p>

  <p class="t charge white" style="top:849px;">Muslim Threat Violence Racism Islamophobia Fear-mongering Extremism Terrorism Hate Authorianism</p>

  <p class="t pillar small left" style="top:923px;">Constitution</p>
  <p class="t pillar small right" style="top:923px;">Shariah Law</p>

  <p class="t title leaf" style="top:862px;font-size:150px;">BESIDE</p>

  <p class="t verb low left" style="top:1035px;">delegitimize</p>
  <p class="t verb low center" style="top:1035px;">destabilize</p>
  <p class="t verb low right" style="top:1035px;">divide</p>

  <p class="t authors center" style="top:1150px;">Imam Kamil Rotheran &amp; Dennis Holt</p>
</main>
</body>
</html>
```